KettlesArmsPersonal

I am a cutting edge, top of the line gun store. We are expanding faster than we can keep up. We offer: Gunsmithing, Transfers, Concealed Carry, Machine Guns, Suppressors. My colors are reflected in my logo. Red, black and white. I like a clean design that gets the point across. I was trying to find a plastic business card, but will settle with a high quality paper product.

Industry/Entity Type

Plastic

Contact Information for Business Card

Dwayne Kettle - Owner
620-555-0148 (Cell)
Kettle's Arms Outfitters
4117 E. Hwy 9
Cedarbend, KS 67099
sales@kettlesarmsoutfitters.example
kettlesarmsoutfitters.example

```html
<!DOCTYPE html>
<html lang="en">
<head>
<meta charset="utf-8">
<title>Kettle's Arms Outfitters – Business Card</title>
<link rel="stylesheet" href="https://fonts.googleapis.com/css2?family=Open+Sans:wght@400;600;700&display=swap">
<style>
  :root {
    --backdrop: #e4e4e4;
    --paper: #f7f6f3;
    --panel: #ffffff;
    --ink: #1c1c1c;
    --grey: #4a4a4a;
    --red: #7a1a14;
    --shadow: rgba(0,0,0,0.25);
  }
  html, body {
    margin: 0;
    width: 1200px;
    height: 675px;
    overflow: hidden;
    background: var(--backdrop);
    font-family: "Open Sans", Arial, sans-serif;
  }
  .canvas {
    position: relative;
    width: 1200px;
    height: 675px;
    display: flex;
    align-items: center;
    justify-content: center;
    gap: 60px;
  }
  .card {
    position: relative;
    width: 520px;
    height: 300px;
    background: var(--paper);
    box-shadow: 0 6px 18px var(--shadow);
    box-sizing: border-box;
  }
  /* Front */
  .card-front { padding: 26px; }
  .front-panel {
    width: 100%;
    height: 100%;
    background: var(--panel);
    display: flex;
    align-items: center;
    justify-content: center;
  }
  .brand {
    display: flex;
    align-items: center;
    gap: 12px;
    color: var(--ink);
    font-weight: 700;
    letter-spacing: 0.04em;
    text-transform: uppercase;
    line-height: 1.25;
  }
  .brand-mark {
    background: var(--red);
    flex: none;
  }
  .brand-lg { font-size: 26px; }
  .brand-lg .brand-mark { width: 22px; height: 22px; }
  .brand-sm { font-size: 12px; gap: 7px; }
  .brand-sm .brand-mark { width: 11px; height: 11px; }
  /* Back */
  .card-back {
    display: flex;
    align-items: center;
    padding: 0 24px 0 22px;
    gap: 18px;
  }
  .back-brand { width: 150px; flex: none; }
  .contact { flex: 1; min-width: 0; }
  .company-name {
    margin: 0 0 4px;
    font-size: 23px;
    font-weight: 400;
    color: var(--grey);
    text-transform: uppercase;
    letter-spacing: -0.01em;
    white-space: nowrap;
  }
  .company-name .accent { color: var(--red); }
  .contact-list {
    margin: 0;
    padding: 0;
    list-style: none;
    font-size: 12.5px;
    line-height: 1.45;
    color: var(--grey);
    white-space: nowrap;
  }
  .contact-person { color: var(--red); }
  .contact-person .role { color: var(--grey); }
</style>
</head>
<body>
<main class="canvas">
  <section class="card card-front" aria-label="Card front">
    <div class="front-panel">
      <div class="brand brand-lg">
        <span class="brand-mark"></span>
        <span class="brand-name">Kettle's Arms Outfitters</span>
      </div>
    </div>
  </section>

  <section class="card card-back" aria-label="Card back">
    <div class="back-brand">
      <div class="brand brand-sm">
        <span class="brand-mark"></span>
        <span class="brand-name">Kettle's Arms Outfitters</span>
      </div>
    </div>
    <div class="contact">
      <h1 class="company-name">Kettle's <span class="accent">Arms</span> Outfitters</h1>
      <ul class="contact-list">
        <li class="contact-person">Dwayne Kettle - <span class="role">Owner</span></li>
        <li>4117 E. Hwy 9 Cedarbend, KS 67099</li>
        <li>cell:&nbsp; 620-555-0148</li>
        <li>email: sales@kettlesarmsoutfitters.example</li>
        <li>website: kettlesarmsoutfitters.example</li>
      </ul>
    </div>
  </section>
</main>
</body>
</html>
```